New Business Card

We need to refresh our business cards. We designed these ourselves and we have no graphic design experience. We would like to find a new business card design that is professional and unique. We are an auto finance company. Feel free to play with the logo, but we would like to keep the eye very present on the card. Our corporate colors are green, grey, and white.
Green - RGB - 168,215,27; HEX - #AADD22
Grey - RGB - 196,196,196; HEX - #C4C4C4
Updates
Need to upload the vector file to finalize the project. The last logo was for a jpeg that didn't stretch well.
Industry/Entity Type
Financial Service
Contact Information for Business Card
Honestly don't know...I need your help!

```html
<!DOCTYPE html>
<html lang="en">
<head>
<meta charset="utf-8">
<title>Brightview Capital – Business Card</title>
<link rel="stylesheet" href="https://fonts.googleapis.com/css2?family=Open+Sans:wght@400;600;700&display=swap">
<style>
  :root {
    --brand-green: #a8d71b;
    --brand-grey: #c4c4c4;
    --card-white: #f7f7f7;
    --text-grey: #6b6b6b;
    --line-grey: #d6d6d6;
    --page-bg: #e9e9e9;
  }
  * { box-sizing: border-box; margin: 0; padding: 0; }
  html, body { width: 1200px; height: 786px; overflow: hidden; }
  body {
    background: var(--page-bg);
    font-family: "Open Sans", Arial, sans-serif;
    display: flex;
    align-items: center;
    justify-content: center;
    gap: 60px;
  }
  .card {
    position: relative;
    width: 510px;
    height: 292px;
    border-radius: 16px;
    overflow: hidden;
    box-shadow: 0 4px 14px rgba(0,0,0,0.12);
  }
  /* Front */
  .card-front { background: var(--card-white); }
  .front-swoosh { position: absolute; inset: 0; width: 100%; height: 100%; }
  .front-brand {
    position: absolute;
    left: 34px;
    top: 96px;
    width: 200px;
    display: flex;
    align-items: center;
    gap: 10px;
  }
  .brand-dot {
    width: 30px; height: 30px; border-radius: 50%;
    background: var(--brand-green); flex: none;
  }
  .brand-name {
    color: var(--brand-green);
    font-weight: 600;
    font-size: 25px;
    line-height: 1.1;
  }
  .divider {
    position: absolute;
    left: 252px; top: 70px;
    width: 1px; height: 120px;
    background: var(--line-grey);
  }
  .contact {
    position: absolute;
    left: 272px; top: 68px;
    color: var(--text-grey);
    font-size: 12px;
    line-height: 1.45;
  }
  .contact-name {
    color: var(--brand-green);
    font-weight: 700;
    font-size: 14px;
    letter-spacing: 0.3px;
    text-transform: uppercase;
  }
  .contact-title { font-size: 12.5px; margin-bottom: 4px; }
  .contact-list { list-style: none; }
  .contact-list li { display: flex; align-items: center; gap: 7px; }
  .contact-list svg { width: 11px; height: 11px; flex: none; }
  .contact-address { margin-top: 6px; }
  /* Back */
  .card-back {
    background: var(--brand-green);
    display: flex; align-items: center; justify-content: center; gap: 14px;
  }
  .card-back .brand-dot { background: #fff; width: 46px; height: 46px; }
  .card-back .brand-name { color: #fff; font-size: 38px; }
</style>
</head>
<body>
  <section class="card card-front" aria-label="Card front">
    <svg class="front-swoosh" viewBox="0 0 510 292" preserveAspectRatio="none" aria-hidden="true">
      <path d="M0 190 C 70 215, 150 250, 215 292 L 0 292 Z" fill="var(--brand-grey)"/>
      <path d="M0 205 C 60 230, 130 262, 180 292 L 0 292 Z" fill="var(--brand-green)"/>
    </svg>
    <div class="front-brand">
      <span class="brand-dot"></span>
      <span class="brand-name">Brightview Capital</span>
    </div>
    <div class="divider"></div>
    <div class="contact">
      <p class="contact-name">Jordan Ellis</p>
      <p class="contact-title">General Manager</p>
      <ul class="contact-list">
        <li>
          <svg viewBox="0 0 12 12"><rect x="3" y="0.5" width="6" height="11" rx="1.2" fill="none" stroke="var(--brand-green)" stroke-width="1.3"/><circle cx="6" cy="9.3" r="0.8" fill="var(--brand-green)"/></svg>
          555-201-4837
        </li>
        <li>
          <svg viewBox="0 0 12 12"><path d="M2.5 1 L4.5 1 L5.3 3.6 L4 4.6 C4.6 6 6 7.4 7.4 8 L8.4 6.7 L11 7.5 L11 9.5 C11 10.4 10.2 11 9.3 11 C4.7 10.6 1.4 7.3 1 2.7 C1 1.8 1.6 1 2.5 1 Z" fill="var(--brand-green)"/></svg>
          555-201-4838
        </li>
        <li>
          <svg viewBox="0 0 12 12"><rect x="0.5" y="2" width="11" height="8" rx="1" fill="var(--brand-green)"/><path d="M1 2.6 L6 6.5 L11 2.6" fill="none" stroke="#fff" stroke-width="1"/></svg>
          info@brightviewcap.com
        </li>
        <li>
          <svg viewBox="0 0 12 12"><circle cx="6" cy="6" r="5.3" fill="none" stroke="var(--brand-green)" stroke-width="1.2"/><ellipse cx="6" cy="6" rx="2.2" ry="5.3" fill="none" stroke="var(--brand-green)" stroke-width="1"/><path d="M0.8 6 H11.2" stroke="var(--brand-green)" stroke-width="1"/></svg>
          www.brightviewcap.com
        </li>
      </ul>
      <p class="contact-address">402 Maple Ridge Rd.<br>Franklin, TN 37064</p>
    </div>
  </section>

  <section class="card card-back" aria-label="Card back">
    <span class="brand-dot"></span>
    <span class="brand-name">Brightview Capital</span>
  </section>
</body>
</html>
```